Deaths in the gang

Creation of a cover for the book "Un soir de cendre" (Title to be used, not the English one)
Size: 14 x 20.5 cm (vertical; with bleed-off on the top, the right side and the bottom)
Title: “An evening of ashes” (this title has no meaning, it's just an expression)
Author: "Fabrice Delvaune"
Publisher: “Editions Marbrel” (at the bottom of the page).
Key Words:
gangster, escape, hold up, murders, jewels, love, young woman with auburn hair.
Story:
Gilles Ferrand, a very dangerous gangster and unscrupulous murderer, escapes from prison in order to organize a new hold up. Lieutenant Voisin, one of the police officers in charge of the investigation falls in love with Sylvie Mabrot, a lovely prison supervisor who has been held hostage during the escape of Ferrand.
But Voisin realizes that Sylvie doesn't tell him all the truth.
And soon, several members of the gang die in mysterious circumstances…
The unbelievable truth will be revealed tardily.
Target Market(s)
Readers of detective stories
Industry/Entity Type
Book
Look and feel

```html
<!DOCTYPE html>
<html lang="fr">
<head>
<meta charset="utf-8">
<title>Un soir de cendre — Fabrice Delvaune</title>
<link rel="stylesheet" href="https://fonts.googleapis.com/css2?family=Cinzel:wght@600;700&family=Rubik+Dirt&display=swap">
<style>
  :root {
    --blood: #8c0006;
    --cream: #f7f3dc;
    --ink: #050303;
  }
  html, body {
    margin: 0;
    padding: 0;
    overflow: hidden;
    background: #222;
  }
  .cover {
    position: relative;
    width: 820px;
    height: 1200px;
    overflow: hidden;
    background: var(--blood);
  }
  .backdrop {
    position: absolute;
    inset: 0;
  }
  .author {
    position: absolute;
    top: 30px;
    left: 0;
    width: 820px;
    margin: 0;
    text-align: center;
    font-family: "Cinzel", serif;
    font-weight: 700;
    font-size: 48px;
    letter-spacing: 12px;
    color: var(--cream);
    text-transform: uppercase;
    white-space: nowrap;
  }
  .title {
    position: absolute;
    left: 0;
    top: 508px;
    width: 820px;
    margin: 0;
    font-family: "Rubik Dirt", system-ui, sans-serif;
    font-weight: 400;
    font-size: 92px;
    line-height: 102px;
    letter-spacing: 2px;
    color: var(--cream);
    text-transform: uppercase;
    white-space: nowrap;
  }
  .title-line {
    display: block;
  }
  .title-line--first {
    padding-left: 138px;
  }
  .title-line--second {
    text-align: right;
    padding-right: 100px;
  }
  .publisher {
    position: absolute;
    bottom: 28px;
    left: 0;
    width: 820px;
    margin: 0;
    text-align: center;
    font-family: "Cinzel", serif;
    font-weight: 700;
    font-size: 22px;
    letter-spacing: 4px;
    color: var(--cream);
    text-transform: uppercase;
    white-space: nowrap;
  }
</style>
</head>
<body>
<main class="cover">
  <svg class="backdrop" width="820" height="1200" viewBox="0 0 820 1200">
    <defs>
      <linearGradient id="figure-fill" x1="0" y1="0" x2="0" y2="1">
        <stop offset="0" stop-color="#050303"/>
        <stop offset="0.6" stop-color="#0a0303"/>
        <stop offset="0.8" stop-color="#5a0606"/>
        <stop offset="1" stop-color="#c8261e"/>
      </linearGradient>
      <radialGradient id="figure-glow" cx="0.5" cy="0.5" r="0.5">
        <stop offset="0" stop-color="#fff6f0"/>
        <stop offset="0.3" stop-color="#ff6a5a" stop-opacity="0.85"/>
        <stop offset="1" stop-color="#c01010" stop-opacity="0"/>
      </radialGradient>
      <radialGradient id="figure-edge" cx="0.5" cy="0.45" r="0.6">
        <stop offset="0.75" stop-color="#050303" stop-opacity="0"/>
        <stop offset="1" stop-color="#8c0006" stop-opacity="0.6"/>
      </radialGradient>
    </defs>
    <path class="splatter-field" fill="var(--cream)"
      d="M820 480 C790 490 755 505 730 525 L730 1200 L820 1200 Z
         M0 700 C30 710 60 730 90 760 L100 1200 L0 1200 Z"/>
    <g role="img" aria-label="Silhouette of a gangster holding a pistol, with a young woman walking down a glowing red corridor">
      <rect x="80" y="110" width="660" height="1090" rx="120" fill="url(#figure-fill)"/>
      <rect x="80" y="110" width="660" height="1090" rx="120" fill="url(#figure-edge)"/>
      <ellipse cx="444" cy="828" rx="140" ry="120" fill="url(#figure-glow)"/>
    </g>
  </svg>

  <p class="author">Fabrice Delvaune</p>

  <h1 class="title">
    <span class="title-line title-line--first">Un soir</span>
    <span class="title-line title-line--second">de cendre</span>
  </h1>

  <p class="publisher">Editions Marbrel</p>
</main>
</body>
</html>
```